Inspirational Quote Poster for Employees

For this project, we need a simple yet high-impact poster template that will be customized for each of our employees with a personalized inspirational quote and color scheme. This template should allow us to quickly and easily customize the text and colors in the poster without a lot of effort.

The poster design should consist of:
- A stylized text area to contain the main text of the quote
- A separate text area to contain the source of quote
- A background that complements the color and style of the text

Text may use different typographic effects (such as color, stroke weight, italicization, font size changes, drop shadows) to draw attention to words in the quote; the source of the quote may be formatted the same as the main text of the quote, or may be formatted differently to distinguish it from the main quote.

The background may be simply a single color, subtle texture, gradients, halftone effects, or other color/texture effects may be used to complement the text.

Examples of the types of posters envisioned by this project:
- http://www.tackvale.com/corwinpmaddox/artquarry-job-1/

Sample quotes to use to build your poster - choose whichever one you want, but be certain that the poster design will handle both long and short quotes:
- "Happiness in intelligent people is the rarest thing I know" - Bertram Faulconer
- "Wanting to be someone else is a waste of the person you are." - Miles Tavenor
- "Experience is not what happens to you. It is what you do with what happens to you." - Cyril Pembrage
- "Simplicity is the ultimate in sophistication." - Ottaviano Restelli
- "You will get all you want in life if you help enough other people get what they want." - Hap Dunmore
- "Hell, there are no rules here — we're trying to accomplish something." - Walter Brisbane

Quote

• Final deliverable must be:
• - Formatted for an 18” x 24” poster (in portrait orientation)
• - Delivered in Adobe InDesign, Adobe Illustrator, or Extended PostScript format
• - Use CMYK color mode
• - Be print-ready at 300dpi resolution
• - Include any fonts used in the template

```html
<!DOCTYPE html>
<html lang="en">
<head>
<meta charset="utf-8">
<title>Quote Poster — Miles Tavenor</title>
<link rel="stylesheet" href="https://fonts.googleapis.com/css2?family=Courgette&family=Mulish:wght@700&display=swap">
<style>
  :root {
    --bg-light: #4f8fc9;
    --bg-mid: #245a92;
    --bg-dark: #0f2d55;
    --frame-top: #5a4220;
    --frame-bottom: #f5bd3a;
    --text: #ffffff;
  }
  html, body {
    margin: 0;
    padding: 0;
    overflow: hidden;
    background: var(--bg-dark);
  }
  .poster {
    position: relative;
    width: 848px;
    height: 1200px;
    overflow: hidden;
  }
  .poster-background {
    position: absolute;
    inset: 0;
    background:
      radial-gradient(ellipse 60% 40% at 58% 14%, var(--bg-light) 0%, rgba(79,143,201,0) 100%),
      linear-gradient(180deg, var(--bg-mid) 0%, #1d4c80 45%, var(--bg-dark) 100%);
  }
  .poster-frame {
    position: absolute;
    inset: 0;
  }
  .quote {
    position: absolute;
    left: 0;
    right: 0;
    top: 246px;
    margin: 0;
    text-align: center;
    font-family: "Courgette", cursive;
    font-size: 92px;
    line-height: 118px;
    color: var(--text);
    text-shadow: 1px 2px 3px rgba(0, 0, 0, 0.25);
  }
  .quote-line {
    display: block;
  }
  .quote-source {
    position: absolute;
    left: 0;
    right: 48px;
    top: 1088px;
    margin: 0;
    text-align: center;
    font-family: "Mulish", sans-serif;
    font-weight: 700;
    font-size: 52px;
    color: var(--text);
  }
</style>
</head>
<body>
  <main class="poster">
    <div class="poster-background" role="img" aria-label="Blue damask wallpaper texture, lighter toward the top"></div>

    <svg class="poster-frame" width="848" height="1200" viewBox="0 0 848 1200" aria-hidden="true">
      <defs>
        <linearGradient id="frame-stroke" x1="0" y1="0" x2="0" y2="1">
          <stop offset="0" stop-color="var(--frame-top)" style="stop-color: var(--frame-top)"/>
          <stop offset="1" stop-color="var(--frame-bottom)" style="stop-color: var(--frame-bottom)"/>
        </linearGradient>
      </defs>
      <rect x="23" y="21" width="802" height="1154" rx="125" ry="125"
            fill="none" stroke="url(#frame-stroke)" stroke-width="9"/>
    </svg>

    <blockquote class="quote">
      <span class="quote-line">Wanting to be</span>
      <span class="quote-line">someone else</span>
      <span class="quote-line">is a waste of</span>
      <span class="quote-line">the person</span>
      <span class="quote-line">you are.</span>
    </blockquote>

    <p class="quote-source">- by Miles Tavenor</p>
  </main>
</body>
</html>
```